I have a tallow based business and I want to streamline my products

I have roughly 10 items that I would like to make lebals for in order to streamline my business, I am attaching the current design and am willing to work with this but would also like to see if you come up with something different, my biggest seller is my facewash , my webpage is theplumwrenco,com my current designs are below- The newest one is the light brown version which I do like but I am not sure how that will integrate or be streamlined with the remaining products, If you believe it can look similar and still be attractive, I am ok with that too,

My current Label Project Needs:

Tallow + Magnesium Lotion biodegradable wheat bottle
Tallow Cream Face Wash - biodegradable what bottle
Tallow Body Butter 8 oz jar with bamboo lid
Tallow Deodorant will be printed on a Kraft Paper tube
Tallow Face Cream for Day wear 2 oz glass jar with bamboo lid
Vitamin C Serum 2 oz serum bottle with bamboo pump
Blue Algae Toner 4 oz glass bottle
Tallow + Hyaluronic 2oz face cream jar
'
My project is to display sustainable products, eco friendly packaging, organic , natural and holistic

I am ok with the newest label I attached but I am also ok with a minimalistic project, I would love to choose from a couple of designs.

Thank you so much

```html
<!DOCTYPE html>
<html lang="en">
<head>
<meta charset="utf-8">
<title>The Plum Wren Co. – Tallow Cream Face Wash Label</title>
<link rel="stylesheet" href="https://fonts.googleapis.com/css2?family=Oswald:wght@300;500;600;700&family=Parisienne&display=swap">
<style>
  :root {
    --backdrop: #eedbb6;
    --label: #ffffff;
    --teal: #0b7ea2;
    --sun: #f5a623;
    --sun-soft: #f8c15d;
  }
  * { margin: 0; padding: 0; box-sizing: border-box; }
  html, body {
    width: 1000px;
    height: 1200px;
    overflow: hidden;
    background: var(--backdrop);
  }
  .label {
    position: absolute;
    left: 222px;
    top: 155px;
    width: 556px;
    height: 893px;
    background: var(--label);
    color: var(--teal);
    font-family: "Oswald", sans-serif;
  }
  .brand-name {
    position: absolute;
    top: 45px;
    left: 0;
    width: 100%;
    text-align: center;
    font-weight: 600;
    font-size: 46px;
    letter-spacing: 1px;
    line-height: 1;
  }
  .hero-art {
    position: absolute;
    left: 68px;
    top: 108px;
    width: 420px;
    height: 310px;
    border-radius: 210px 210px 12px 12px;
    background: radial-gradient(circle at 62% 45%, var(--sun-soft) 0%, var(--sun) 45%, var(--teal) 100%);
  }
  .product-title {
    position: absolute;
    left: 0;
    width: 100%;
    text-align: center;
    font-weight: 700;
    line-height: 1;
    letter-spacing: 2px;
  }
  .product-title--face { top: 412px; font-size: 150px; }
  .product-title--wash { top: 565px; font-size: 150px; }
  .product-script {
    position: absolute;
    left: 0;
    top: 500px;
    width: 100%;
    text-align: center;
    font-family: "Parisienne", cursive;
    font-size: 84px;
    line-height: 1;
    color: var(--sun);
    transform: rotate(-4deg);
  }
  .divider {
    position: absolute;
    left: 58px;
    top: 722px;
    width: 440px;
    height: 30px;
  }
  .divider-rule {
    position: absolute;
    top: 13px;
    height: 4px;
    border-radius: 2px;
    background: var(--teal);
  }
  .divider-rule--left { left: 0; width: 185px; }
  .divider-rule--right { right: 0; width: 175px; }
  .divider-mark {
    position: absolute;
    left: 200px;
    top: 0;
    width: 30px;
    height: 30px;
    border-radius: 50%;
    background: var(--teal);
  }
  .benefits {
    position: absolute;
    top: 772px;
    left: 0;
    width: 100%;
    text-align: center;
    font-weight: 500;
    font-size: 31px;
    letter-spacing: 0.5px;
    line-height: 1;
  }
  .net-weight {
    position: absolute;
    top: 836px;
    left: 0;
    width: 100%;
    text-align: center;
    font-weight: 300;
    font-size: 22px;
    line-height: 1;
  }
</style>
</head>
<body>
  <main class="label">
    <p class="brand-name">THE PLUM WREN CO.</p>
    <div class="hero-art" role="img" aria-label="Illustration of a spotted cow standing in front of a rising orange sun with rays"></div>
    <h1 class="product-title product-title--face">FACE</h1>
    <h1 class="product-title product-title--wash">WASH</h1>
    <p class="product-script">Tallow Cream</p>
    <div class="divider">
      <span class="divider-rule divider-rule--left"></span>
      <span class="divider-mark" role="img" aria-label="Small flower ornament"></span>
      <span class="divider-rule divider-rule--right"></span>
    </div>
    <p class="benefits">CLEANSE • PURIFY • MOISTURIZE</p>
    <p class="net-weight">NET WT. 236ML</p>
  </main>
</body>
</html>
```